Rack card for marketing

Office to office marketing for knee pain treatment

Target Market(s)

Medical Offices, Retired patients looking to maintain active lifestlye. Family practice medical offices

Industry/Entity Type

Medical

Colors
0054AA
0677BA
7BADD7
CADEEF
E8F1F8

Requirements
Must have
• Font that matches logo, GRM logo, graphic of a retiree who looks active and happy versus a knee graphic
Nice to have
• The best ever rack card!!! Easy to Read, simplicity is key.

```html
<!DOCTYPE html>
<html lang="en">
<head>
<meta charset="utf-8">
<title>GRM Knee Pain Rack Card</title>
<link href="https://fonts.googleapis.com/css2?family=Roboto+Condensed:wght@400;500;700&display=swap" rel="stylesheet">
<style>
  :root {
    --brand-blue: #23618a;
    --text-blue: #1f5a85;
    --band-gray: #b3b3b3;
    --page-bg: #eeeeee;
    --card-bg: #ffffff;
    --bullet-gray: #a9a9a9;
  }
  * { margin: 0; padding: 0; box-sizing: border-box; }
  html, body { width: 1113px; height: 1200px; overflow: hidden; }
  body { background: var(--page-bg); font-family: "Roboto Condensed", "Arial Narrow", sans-serif; position: relative; }
  .rack-card {
    position: absolute; left: 283px; top: 20px;
    width: 576px; height: 1224px;
    transform: scale(0.948); transform-origin: top left;
    background: var(--card-bg); overflow: hidden;
    box-shadow: 0 4px 14px rgba(0,0,0,0.18);
  }
  .bands { position: absolute; inset: 0; }
  .headline {
    position: absolute; right: 324px; top: 36px;
    text-align: right; color: var(--text-blue);
    font-weight: 500; font-size: 27px; line-height: 28.5px; letter-spacing: 0.5px;
  }
  .divider { position: absolute; left: 283px; top: 22px; width: 3px; height: 143px; background: var(--brand-blue); }
  .brand { position: absolute; left: 330px; top: 50px; color: var(--brand-blue); font-weight: 500; }
  .brand-dot { display: inline-block; width: 14px; height: 14px; border-radius: 50%; background: var(--brand-blue); margin-right: 10px; vertical-align: middle; }
  .brand-name { font-size: 56px; line-height: 56px; vertical-align: middle; }
  .brand-tag { font-size: 22px; line-height: 26px; margin-top: 2px; padding-left: 24px; }
  .knee-photo {
    position: absolute; left: 0; top: 185px; width: 330px; height: 540px;
    background:
      linear-gradient(180deg, rgba(255,255,255,0) 0%, rgba(255,255,255,0) 70%, #ffffff 100%),
      linear-gradient(100deg, #7a7a7a 0%, #b9aba3 35%, #d2c7c0 60%, rgba(235,235,235,0.6) 85%, rgba(255,255,255,0) 100%);
  }
  .ride-photo {
    position: absolute; left: 26px; top: 504px; width: 284px; height: 284px; border-radius: 50%;
    background: radial-gradient(circle at 50% 40%, #d9dccf 0%, #9cb56b 35%, #4f7a2e 75%, #3d6123 100%);
  }
  .benefits {
    position: absolute; left: 310px; top: 264px; list-style: none;
    color: var(--text-blue); font-size: 23px; line-height: 29.6px; letter-spacing: 0.4px;
  }
  .benefits li { padding-left: 17px; position: relative; }
  .benefits li::before {
    content: ""; position: absolute; left: 0; top: 12px; width: 7px; height: 7px; border-radius: 50%; background: var(--bullet-gray);
  }
  .benefits .sub { display: block; padding-left: 20px; }
  .benefits .sub-deep { display: block; padding-left: 34px; }
  .procedures { position: absolute; left: 0; right: 0; top: 799px; text-align: center; color: #fff; }
  .procedures-label {
    display: inline-block; background: #fff; color: var(--brand-blue);
    font-weight: 700; font-size: 22px; line-height: 28px; padding: 0 6px; margin-bottom: 4px;
  }
  .procedures-list { list-style: none; font-weight: 700; font-size: 25px; line-height: 32.8px; letter-spacing: 0.5px; }
  .contact { position: absolute; left: 0; right: 0; top: 1070px; text-align: center; color: var(--text-blue); }
  .doctor { font-weight: 500; font-size: 31px; line-height: 36px; letter-spacing: 0.5px; }
  .practice { font-weight: 500; font-size: 20px; line-height: 24px; letter-spacing: 1px; }
  .address, .phones { font-weight: 500; font-size: 21.5px; line-height: 32px; letter-spacing: 0.8px; }
  .address { margin-top: 7px; }
  .phones span + span { margin-left: 18px; }
</style>
</head>
<body>
  <main class="rack-card">
    <div class="knee-photo" role="img" aria-label="Photo of a person holding a painful knee"></div>

    <svg class="bands" width="576" height="1224" viewBox="0 0 576 1224" aria-hidden="true">
      <path d="M0,220 Q288,142 576,220 L576,262 Q288,118 0,262 Z" fill="var(--brand-blue)"/>
      <path d="M0,718 Q288,838 576,718 L576,800 L0,800 Z" fill="var(--band-gray)"/>
      <path d="M0,1030 L576,1030 L576,1098 Q288,998 0,1098 Z" fill="var(--band-gray)"/>
      <path d="M0,746 Q288,820 576,746 L576,1068 Q288,1018 0,1068 Z" fill="var(--brand-blue)"/>
    </svg>

    <div class="ride-photo" role="img" aria-label="Happy active retired couple riding bicycles in a green park"></div>

    <h1 class="headline">Comprehensive<br>Non-operative<br>Treatment<br>for Knee Pain</h1>
    <div class="divider"></div>
    <div class="brand">
      <div><span class="brand-dot"></span><span class="brand-name">GRM</span></div>
      <div class="brand-tag">Gulf Ridge Medical</div>
    </div>

    <ul class="benefits">
      <li>Nonsurgical Options</li>
      <li>Customized Bracing</li>
      <li>Topical Medications</li>
      <li>Topical Supplements</li>
      <li>Evidence Based<span class="sub">Supplementation</span></li>
      <li>Cryotherapy /<span class="sub">Cold Compression</span></li>
      <li>Acupuncture /<span class="sub">Electrical Therapy</span></li>
      <li>Exercise Protocols<span class="sub">Athletic Trainer</span><span class="sub">Exercise Physiologist</span><span class="sub">Home based</span><span class="sub-deep">exercise options</span></li>
    </ul>

    <section class="procedures">
      <h2 class="procedures-label">Procedures Offered</h2>
      <ul class="procedures-list">
        <li>Interarticular Knee Injection</li>
        <li>Pes Anserine Bursa</li>
        <li>Genicular Nerve Block</li>
        <li>Genicular Radiofrequency Ablation</li>
        <li>HA (hyaluronic acid) Injections</li>
        <li>Arnicel Injections</li>
      </ul>
    </section>

    <footer class="contact">
      <p class="doctor">Martin Kessler, M.D.</p>
      <p class="practice">Lakeview Pain Management</p>
      <p class="address">1840 Orchard Crest Blvd., Lakeside, FL 34000</p>
      <p class="phones"><span>Phone 352-555-0142</span><span>Fax 352-555-0187</span></p>
    </footer>
  </main>
</body>
</html>
```